Website for peer to peer car sharing service

Hi all,

We need a web design for a new environmental friendly peer-to-peer car sharing website.

The website will serve as a marketplace where car owners can list their car and drivers that who do not have access to a car can rent a suitable car. It is important for us to emphasis that this is a community where the main purpose is to use the vehicles on the street in a more efficient way.

Attached are five pictures where we have sketched up the five main pages:

File 1. Info site for a particular car.
File 2. Logo.
File 3. Register a car.
File 4. Sign up.
File 5. Search.
File 6. Front page.

The logo for the company is attached (File 2) and it would be ideal to design the website in relation to the logo. The final design should relate to a secure market place which is environmental friendly.

We would like this webpage to be in the same spirit as www.velnoro.it, www.brundale.com, www.plimtrovesite.com, https://wend.kul.net, https://garbelow.com etc.

We look forward to see your designs.

Best regards,
The Trundo Team.

Hi guys, 

Please take :

1) Could you please design icons for for  'FAQ' and 'Insurance' in the header, locate the icons right to the Trundo logo. We only want two icons ('FAQ' and 'Insurance')  right to the Trundo logo.

2) The height of the header should be the same as the header of faplex.com

3) The price tags for the cars (below the top section) should be similar to the price tags at mostanbee.com.

4) We would like you to start to design the other pages (the sub-pages listed in the project description:
a)Info site for a particular car.
b)Register a car. 
c)Search results (similar to http://www.pevrotank.com/find-car).

Please take a look at the picture attached for the sub-pages:

https://files.quenmolt.example/brief_uploads/000001_3_search_000001_brief000001.jpg

https://files.quenmolt.example/brief_uploads/000002_4_infositeforaparticularcar_000002_brief000002.jpg

http://www.quenmolt.example/file.aspx?fileLocation=storage_url/brief_uploads/000003_5_registeracar_brief000003.jpg

Best regards, 
Trundo team 

Target Market(s)

The target market are people from 20-40 years old who are environmental friendly, also tourists who visit the city and would like to rent a car.

Industry/Entity Type

It Company

Requirements
Must have
• It is required that the designer that will be chosen will hand in layered PSD files of each web page.

```html
<!DOCTYPE html>
<html lang="en">
<head>
<meta charset="utf-8">
<title>Trundo – Find a Car</title>
<link href="https://fonts.googleapis.com/css2?family=Questrial&family=Arimo:wght@400;700&display=swap" rel="stylesheet">
<style>
:root{
  --header:#3c3c3c;
  --search-band:#5b5b5b;
  --press-band:#383838;
  --footer:#000;
  --white:#fff;
  --text:#222;
  --muted:#8a8a8a;
  --rule:#dedede;
  --green:#7dc242;
  --green-dark:#5fa22a;
  --star:#f08a00;
  --map-sea:#a9c3df;
  --map-land:#efe9dc;
}
*{box-sizing:border-box;margin:0;padding:0}
html,body{width:1200px;height:1192px;overflow:hidden}
body{position:relative;background:var(--white);font-family:"Arimo",Arial,sans-serif;color:var(--text)}
.abs{position:absolute}

/* header */
.site-header{position:absolute;left:0;top:0;width:1200px;height:44px;background:var(--header);border-bottom:1px solid #2a2a2a}
.brand{position:absolute;left:165px;top:8px;font-family:"Questrial",sans-serif;font-size:24px;color:var(--green);display:flex;align-items:center;gap:8px}
.brand-dot{width:14px;height:14px;border-radius:50%;background:var(--green)}
.header-icon{position:absolute;top:0;height:44px;border-left:1px solid #2a2a2a;display:flex;align-items:center;justify-content:center}
.icon-faq{left:295px;width:52px}
.icon-insurance{left:347px;width:56px;border-right:1px solid #2a2a2a}
.main-nav{position:absolute;top:12px;font-family:"Questrial",sans-serif;font-size:17px;color:var(--white)}

/* search band */
.search-band{position:absolute;left:0;top:45px;width:1200px;height:141px;background:var(--search-band)}
.field-label{position:absolute;top:38px;font-family:"Arimo",sans-serif;font-weight:700;font-size:15px;color:var(--white)}
.select{position:absolute;top:65px;height:30px;background:var(--white);border-radius:3px;font-size:12px;color:#555;padding:8px 12px}
.select::after{content:"";position:absolute;right:10px;top:12px;border:6px solid transparent;border-top:7px solid #444;border-bottom:0}
.find-btn{position:absolute;left:874px;top:64px;width:140px;height:31px;border-radius:5px;background:linear-gradient(#9ee05b,var(--green-dark));color:#1d3a0b;font-size:16px;text-align:center;line-height:31px;font-family:"Questrial",sans-serif}

/* listing */
.listing{position:absolute;left:0;top:186px;width:421px;height:559px;background:var(--white)}
.car{position:absolute;left:0;width:421px;height:139px;border-bottom:2px solid var(--rule)}
.car:last-child{border-bottom:0}
.car-photo{position:absolute;left:11px;top:11px;width:159px;height:111px;border:1px solid #ccc}
.car-name{position:absolute;left:179px;top:17px;font-weight:700;font-size:14px}
.stars{position:absolute;left:180px;top:36px;color:var(--star);font-size:12px;letter-spacing:5px}
.car-city{position:absolute;left:181px;top:58px;font-size:13px;color:var(--muted);display:flex;gap:4px;align-items:center}
.car-owner{position:absolute;left:179px;top:79px;font-size:15px}
.price{position:absolute;right:23px;text-align:right;font-size:11px}
.price b{font-weight:400;font-size:14px}
.p1{top:37px}.p2{top:62px}.p3{top:80px}
.scrollbar{position:absolute;left:421px;top:186px;width:6px;height:559px;background:#d6d6d6}
.scrollbar span{position:absolute;left:0;top:0;width:6px;height:144px;background:#8f8f8f}

/* map */
.map{position:absolute;left:427px;top:186px;width:461px;height:559px;background:linear-gradient(160deg,var(--map-land) 0%,var(--map-land) 38%,var(--map-sea) 52%,var(--map-sea) 100%)}
.map-edge{position:absolute;left:888px;top:186px;width:4px;height:559px;background:#bdbdbd}

/* filters */
.filters{position:absolute;left:892px;top:186px;width:308px;height:559px;background:var(--white)}
.filter-title{position:absolute;left:36px;font-weight:700;color:#444}
.filter-rule{position:absolute;left:36px;width:231px;height:1px;background:var(--rule)}
.range-track{position:absolute;left:37px;top:146px;width:230px;height:6px;border:1px solid #ccc;background:#f4f4f4}
.range-fill{position:absolute;left:96px;top:146px;width:122px;height:6px;background:#555}
.range-knob{position:absolute;top:142px;width:14px;height:14px;background:#f7f7f7;border:1px solid #aaa;border-radius:2px}
.range-label{position:absolute;top:163px;font-size:11px;color:#666;letter-spacing:.5px}
.check{position:absolute;left:38px;display:flex;align-items:center;gap:11px;font-size:14px;color:#666}
.check i{width:13px;height:13px;border:1px solid #999;border-radius:2px;display:block}
.brand-select{position:absolute;left:37px;top:449px;width:231px;height:31px;border:1px solid #bbb;border-radius:5px;font-size:14px;color:#444;padding:6px 12px}
.brand-select::after{content:"";position:absolute;right:12px;top:12px;border:5px solid transparent;border-top:7px solid #444;border-bottom:0}

/* press */
.press{position:absolute;left:0;top:746px;width:1200px;height:169px;background:var(--press-band)}
.press-name{position:absolute;top:68px;font-family:"Arimo",sans-serif;font-weight:700;font-size:24px;color:var(--white)}

/* footer */
.site-footer{position:absolute;left:0;top:915px;width:1200px;height:277px;background:var(--footer);color:var(--white);font-family:"Questrial",sans-serif}
.footer-brand{position:absolute;left:188px;top:80px;font-size:46px;color:#a9a9a9;display:flex;align-items:center;gap:14px}
.footer-brand span{width:36px;height:36px;border-radius:50%;background:#a9a9a9}
.footer-links{position:absolute;left:195px;top:154px;font-size:17px}
.footer-links span{margin:0 9px;color:#bbb}
.copyright{position:absolute;left:192px;top:182px;font-size:15px}
.contact{position:absolute;right:172px;text-align:right;font-size:17px;line-height:22px}
</style>
</head>
<body>

<header class="site-header">
  <div class="brand"><span class="brand-dot"></span>Trundo</div>
  <div class="header-icon icon-faq" aria-label="FAQ">
    <svg width="24" height="22" viewBox="0 0 24 22"><path d="M3 2h18a2 2 0 0 1 2 2v10a2 2 0 0 1-2 2H10l-5 5v-5H3a2 2 0 0 1-2-2V4a2 2 0 0 1 2-2z" fill="#fff"/><path d="M6 7h12M6 11h9" stroke="#3c3c3c" stroke-width="1.8"/></svg>
  </div>
  <div class="header-icon icon-insurance" aria-label="Insurance">
    <svg width="28" height="28" viewBox="0 0 28 28"><circle cx="14" cy="14" r="13" fill="#fff"/><path d="M8 17l1.5-5a2 2 0 0 1 2-1.5h5a2 2 0 0 1 2 1.5l1.5 5v4h-3v-2h-7v2H8z" fill="#3c3c3c"/></svg>
  </div>
  <nav>
    <span class="main-nav" style="left:728px">List your Car</span>
    <span class="main-nav" style="left:867px">Login</span>
    <span class="main-nav" style="left:954px">Sign up</span>
  </nav>
</header>

<section class="search-band">
  <span class="field-label" style="left:165px">Start Time</span>
  <div class="select" style="left:165px;width:115px">2013-08-05</div>
  <div class="select" style="left:286px;width:85px">10:00</div>
  <span class="field-label" style="left:411px">End Time</span>
  <div class="select" style="left:411px;width:115px">2013-08-05</div>
  <div class="select" style="left:532px;width:85px">10:00</div>
  <span class="field-label" style="left:655px">Location</span>
  <div class="select" style="left:654px;width:175px">California</div>
  <div class="find-btn">Find a Car</div>
</section>

<section class="listing">
  <article class="car" style="top:0">
    <div class="car-photo" role="img" aria-label="Photo of a dark grey estate car parked outdoors" style="background:linear-gradient(#6f8f5a 0%,#4a5a3e 45%,#3b3f45 70%,#9a9a92 100%)"></div>
    <div class="car-name">Halvern Legate</div>
    <div class="stars">★★★★★</div>
    <div class="car-city"><svg width="9" height="12" viewBox="0 0 9 12"><path d="M4.5 0A4.5 4.5 0 0 0 0 4.5C0 8 4.5 12 4.5 12S9 8 9 4.5A4.5 4.5 0 0 0 4.5 0z" fill="#aaa"/><circle cx="4.5" cy="4.5" r="1.6" fill="#fff"/></svg>San Francisco</div>
    <div class="car-owner">Tobin</div>
    <div class="price p1"><b>$ 10</b> /hour</div>
    <div class="price p2">$ 60/day</div>
    <div class="price p3">$ 120/week</div>
  </article>
  <article class="car" style="top:138px">
    <div class="car-photo" role="img" aria-label="Photo of a grey sedan in front of a metal wall" style="background:linear-gradient(#4f78a8 0%,#9aa3a8 30%,#5a6068 65%,#b9b7b0 100%)"></div>
    <div class="car-name">Korvan Jeston</div>
    <div class="stars">★★★★★</div>
    <div class="car-city"><svg width="9" height="12" viewBox="0 0 9 12"><path d="M4.5 0A4.5 4.5 0 0 0 0 4.5C0 8 4.5 12 4.5 12S9 8 9 4.5A4.5 4.5 0 0 0 4.5 0z" fill="#aaa"/><circle cx="4.5" cy="4.5" r="1.6" fill="#fff"/></svg>San Francisco</div>
    <div class="car-owner">Ned Calloway</div>
    <div class="price p1"><b>$ 10</b> /hour</div>
    <div class="price p2">$ 60/day</div>
    <div class="price p3">$ 120/week</div>
  </article>
  <article class="car" style="top:278px">
    <div class="car-photo" role="img" aria-label="Photo of a small turquoise hatchback" style="background:linear-gradient(#d8d8d6 0%,#c4c6c4 35%,#3aa6c4 60%,#8c8c88 100%)"></div>
    <div class="car-name">Pipa Coupe</div>
    <div class="stars">★★★★★</div>
    <div class="car-city"><svg width="9" height="12" viewBox="0 0 9 12"><path d="M4.5 0A4.5 4.5 0 0 0 0 4.5C0 8 4.5 12 4.5 12S9 8 9 4.5A4.5 4.5 0 0 0 4.5 0z" fill="#aaa"/><circle cx="4.5" cy="4.5" r="1.6" fill="#fff"/></svg>San Francisco</div>
    <div class="car-owner">Ilsa</div>
    <div class="price p1"><b>$ 10</b> /hour</div>
    <div class="price p2">$ 60/day</div>
    <div class="price p3">$ 120/week</div>
  </article>
  <article class="car" style="top:421px">
    <div class="car-photo" role="img" aria-label="Photo of a grey sedan in front of a metal wall" style="background:linear-gradient(#4f78a8 0%,#9aa3a8 30%,#5a6068 65%,#b9b7b0 100%)"></div>
    <div class="car-name">Korvan Jeston</div>
    <div class="stars">★★★★★</div>
    <div class="car-city"><svg width="9" height="12" viewBox="0 0 9 12"><path d="M4.5 0A4.5 4.5 0 0 0 0 4.5C0 8 4.5 12 4.5 12S9 8 9 4.5A4.5 4.5 0 0 0 4.5 0z" fill="#aaa"/><circle cx="4.5" cy="4.5" r="1.6" fill="#fff"/></svg>San Francisco</div>
    <div class="car-owner">Ned Calloway</div>
    <div class="price p1"><b>$ 10</b> /hour</div>
    <div class="price p2">$ 60/day</div>
    <div class="price p3">$ 120/week</div>
  </article>
</section>
<div class="scrollbar"><span></span></div>

<div class="map" role="img" aria-label="Street map of the search area with orange markers for available cars"></div>
<div class="map-edge"></div>

<aside class="filters">
  <div class="filter-title" style="top:30px;font-size:17px">Filters</div>
  <div class="filter-rule" style="top:72px"></div>
  <div class="filter-title" style="top:105px;font-size:15px">Price Range</div>
  <div class="range-track"></div>
  <div class="range-fill"></div>
  <div class="range-knob" style="left:89px"></div>
  <div class="range-knob" style="left:210px"></div>
  <div class="range-label" style="left:37px">$50</div>
  <div class="range-label" style="left:232px">$5000</div>
  <div class="filter-rule" style="top:212px"></div>
  <div class="filter-title" style="top:249px;font-size:15px">Car Types</div>
  <div class="check" style="top:279px"><i></i>Cars</div>
  <div class="check" style="top:306px"><i></i>Vans</div>
  <div class="check" style="top:334px"><i></i>Trucks</div>
  <div class="filter-rule" style="top:392px"></div>
  <div class="filter-title" style="top:422px;font-size:15px">Car Brands</div>
  <div class="brand-select">Morana</div>
</aside>

<section class="press">
  <span class="press-name" style="left:190px">The Daily Ledger</span>
  <span class="press-name" style="left:528px">Nation Post</span>
  <span class="press-name" style="left:816px">Coastal Herald</span>
</section>

<footer class="site-footer">
  <div class="footer-brand"><span></span>Trundo</div>
  <div class="footer-links">About<span>|</span>Contact Us<span>|</span>Privacy Policy<span>|</span>Blog</div>
  <div class="copyright">© 2013 Trundo. All Rights Reserved.</div>
  <div class="contact" style="top:83px">mara@plimtrovesite.com<br>1.555.204.7719</div>
  <div class="contact" style="top:159px">4120 Larkwood Ave. #31058<br>Fenmoor, CA 90412.</div>
</footer>

</body>
</html>
```